Banner Design for Holistic Clinic

We need a banner to be designed for a Holistic Clinic which treats patient using IV Nutrition therapy, IV Vitamin C therapy, Chelation therapy, Homoepathy , Accupuncture, Ayurveda. Our website is www.verdantcarehub.in

We need the banner to show case all our services. IV Nutrition therapy, IV Vitamin C therapy, Chelation therapy, Homoepathy , Accupuncture, Ayurveda with special emphasis on IV Therapies. This will be in the front of the web page and will be used for leaflets and flex material.Ideally

I like the concept of IV infsuion bags, fruits etc. I have attached some of the pic which i liked. Please see the attachment "banner clinic july 13" But feel free to change it and bring in something better that will showcase all our services together

Target Market(s)

30 plus Adults

Industry/Entity Type

Health And Wellness

Font styles to use
Serif

Colors
acd036
f37122
33a6d7

Requirements
Must have
• Some samples are given below. It got to be colourful, yet pleasing.

```html
<!DOCTYPE html>
<html lang="en">
<head>
<meta charset="utf-8">
<title>Holistic Clinic Services Banner</title>
<link rel="stylesheet" href="https://fonts.googleapis.com/css2?family=Tinos:wght@700&display=swap">
<style>
  :root {
    --stage: #363737;
    --field: #8ab333;
    --field-light: #97c03a;
    --frame: #a9d23c;
    --label: #ffffff;
  }
  html, body {
    margin: 0;
    padding: 0;
    width: 1200px;
    height: 1200px;
    overflow: hidden;
    background: var(--stage);
  }
  .banner {
    position: absolute;
    left: 89px;
    top: 386px;
    width: 1022px;
    height: 426px;
    box-shadow: 0 6px 14px rgba(0,0,0,0.45);
  }
  .banner svg { display: block; }
  .service-label {
    font-family: "Tinos", "Times New Roman", serif;
    font-weight: 700;
    font-size: 11px;
    fill: var(--label);
    letter-spacing: 0.2px;
  }
  .cord { stroke: var(--frame); stroke-width: 3; fill: none; }
  .hook { stroke: var(--frame); stroke-width: 5; fill: none; }
  .bag-frame { fill: none; stroke: var(--frame); stroke-width: 6; stroke-linejoin: round; }
  .connector { fill: var(--frame); }
</style>
</head>
<body>
<div class="banner">
<svg width="1022" height="426" viewBox="0 0 1022 426" xmlns="http://www.w3.org/2000/svg">
  <defs>
    <linearGradient id="field" x1="0" y1="0" x2="1" y2="1">
      <stop offset="0" stop-color="#95bd37"/>
      <stop offset="0.5" stop-color="#88b032"/>
      <stop offset="1" stop-color="#8fb835"/>
    </linearGradient>
    <linearGradient id="leaves" x1="0" y1="0" x2="0" y2="1">
      <stop offset="0" stop-color="#9fcf3a" stop-opacity="0"/>
      <stop offset="1" stop-color="#a6d13e" stop-opacity="0.85"/>
    </linearGradient>
    <linearGradient id="produce" x1="0" y1="0" x2="1" y2="1">
      <stop offset="0" stop-color="#6f9a2e"/><stop offset="0.5" stop-color="#c8452c"/><stop offset="1" stop-color="#e5a52a"/>
    </linearGradient>
    <linearGradient id="citrus" x1="0" y1="0" x2="1" y2="1">
      <stop offset="0" stop-color="#f7a629"/><stop offset="1" stop-color="#f08a1c"/>
    </linearGradient>
    <linearGradient id="blood" x1="0" y1="0" x2="1" y2="1">
      <stop offset="0" stop-color="#e0605c"/><stop offset="1" stop-color="#a8262a"/>
    </linearGradient>
    <linearGradient id="remedy" x1="0" y1="0" x2="0" y2="1">
      <stop offset="0" stop-color="#7a5a2e"/><stop offset="0.6" stop-color="#b58255"/><stop offset="1" stop-color="#d8c2a8"/>
    </linearGradient>
    <linearGradient id="needles" x1="0" y1="0" x2="0" y2="1">
      <stop offset="0" stop-color="#f4f5f7"/><stop offset="0.6" stop-color="#e7d0c3"/><stop offset="1" stop-color="#c9a08a"/>
    </linearGradient>
    <linearGradient id="herbal" x1="0" y1="0" x2="1" y2="1">
      <stop offset="0" stop-color="#c9aa5a"/><stop offset="0.5" stop-color="#b89a3a"/><stop offset="1" stop-color="#8a9a3a"/>
    </linearGradient>
    <path id="bag-shape" d="M -65,8 Q -65,0 -57,0 L 57,0 Q 65,0 65,8 L 65,110 L 4,162 Q 0,165 -4,162 L -65,110 Z"/>
  </defs>

  <rect class="background" width="1022" height="426" fill="url(#field)"/>
  <rect class="leaf-band" role="img" aria-label="Fresh green leaves along the bottom edge" x="0" y="340" width="1022" height="86" fill="url(#leaves)"/>

  <!-- Service bags -->
  <g class="service" transform="translate(216.1,34.8)">
    <line class="cord" x1="0" y1="-35" x2="0" y2="-18"/>
    <circle class="hook" cx="0" cy="-10" r="8"/>
    <use href="#bag-shape" fill="url(#produce)" role="img" aria-label="Colourful fresh vegetables and fruit"/>
    <use href="#bag-shape" class="bag-frame"/>
    <rect class="connector" x="-7" y="164" width="14" height="12"/>
    <rect class="connector" x="-11" y="176" width="22" height="28"/>
    <line class="cord" x1="-5" y1="204" x2="-5" y2="392"/>
    <line class="cord" x1="5" y1="204" x2="5" y2="392"/>
  </g>
  <text class="service-label" transform="translate(129.8,107.4) rotate(-90)" text-anchor="middle"><tspan x="0" dy="-3">IV NUTRITION</tspan><tspan x="0" dy="14">THERAPY</tspan></text>

  <g class="service" transform="translate(349,175.6)">
    <line class="cord" x1="0" y1="-176" x2="0" y2="-18"/>
    <circle class="hook" cx="0" cy="-10" r="8"/>
    <use href="#bag-shape" fill="url(#citrus)" role="img" aria-label="Sliced oranges"/>
    <use href="#bag-shape" class="bag-frame"/>
    <rect class="connector" x="-7" y="164" width="14" height="12"/>
    <rect class="connector" x="-11" y="176" width="22" height="28"/>
    <line class="cord" x1="-5" y1="204" x2="-5" y2="251"/>
    <line class="cord" x1="5" y1="204" x2="5" y2="251"/>
  </g>
  <text class="service-label" transform="translate(262.7,241) rotate(-90)" text-anchor="middle"><tspan x="0" dy="-3">IV VITAMIN C</tspan><tspan x="0" dy="14">THERAPY</tspan></text>

  <g class="service" transform="translate(483.2,37.9)">
    <line class="cord" x1="0" y1="-38" x2="0" y2="-18"/>
    <circle class="hook" cx="0" cy="-10" r="8"/>
    <use href="#bag-shape" fill="url(#blood)" role="img" aria-label="Red blood cells inside a vessel"/>
    <use href="#bag-shape" class="bag-frame"/>
    <rect class="connector" x="-7" y="164" width="14" height="12"/>
    <rect class="connector" x="-11" y="176" width="22" height="28"/>
    <line class="cord" x1="-5" y1="204" x2="-5" y2="389"/>
    <line class="cord" x1="5" y1="204" x2="5" y2="389"/>
  </g>
  <text class="service-label" transform="translate(393,95) rotate(-90)" text-anchor="middle"><tspan x="0" dy="-3">CHELATION</tspan><tspan x="0" dy="14">THERAPY</tspan></text>

  <g class="service" transform="translate(606.2,169.4)">
    <line class="cord" x1="0" y1="-170" x2="0" y2="-18"/>
    <circle class="hook" cx="0" cy="-10" r="8"/>
    <use href="#bag-shape" fill="url(#remedy)" role="img" aria-label="Amber bottle with white homeopathic pills"/>
    <use href="#bag-shape" class="bag-frame"/>
    <rect class="connector" x="-7" y="164" width="14" height="12"/>
    <rect class="connector" x="-11" y="176" width="22" height="28"/>
    <line class="cord" x1="-5" y1="204" x2="-5" y2="257"/>
    <line class="cord" x1="5" y1="204" x2="5" y2="257"/>
  </g>
  <text class="service-label" transform="translate(531,227) rotate(-90)" text-anchor="middle" dy="4">HOMOEPATHY</text>

  <g class="service" transform="translate(719.8,37.9)">
    <line class="cord" x1="0" y1="-38" x2="0" y2="-18"/>
    <circle class="hook" cx="0" cy="-10" r="8"/>
    <use href="#bag-shape" fill="url(#needles)" role="img" aria-label="Acupuncture needles placed in skin"/>
    <use href="#bag-shape" class="bag-frame"/>
    <rect class="connector" x="-7" y="164" width="14" height="12"/>
    <rect class="connector" x="-11" y="176" width="22" height="28"/>
    <line class="cord" x1="-5" y1="204" x2="-5" y2="389"/>
    <line class="cord" x1="5" y1="204" x2="5" y2="389"/>
  </g>
  <text class="service-label" transform="translate(641.5,95) rotate(-90)" text-anchor="middle" dy="4">ACCUPUNCTURE</text>

  <g class="service" transform="translate(838.9,172)">
    <line class="cord" x1="0" y1="-172" x2="0" y2="-18"/>
    <circle class="hook" cx="0" cy="-10" r="8"/>
    <use href="#bag-shape" fill="url(#herbal)" role="img" aria-label="Herbal oil, mortar and pestle with fresh leaves"/>
    <use href="#bag-shape" class="bag-frame"/>
    <rect class="connector" x="-7" y="164" width="14" height="12"/>
    <rect class="connector" x="-11" y="176" width="22" height="28"/>
    <line class="cord" x1="-5" y1="204" x2="-5" y2="254"/>
    <line class="cord" x1="5" y1="204" x2="5" y2="254"/>
  </g>
  <text class="service-label" transform="translate(764.5,231.6) rotate(-90)" text-anchor="middle" dy="4">AYURVEDA</text>
</svg>
</div>
</body>
</html>
```